New River III Precinct 6x11 GOTV postcard

We require BOTH persuasive copy and high-impact layout for an oversized 6x11 political mailer. This might be one person, but it likely requires a specialized "creative team." of an experienced political strategist copywriter PLUS a graphic designer - so the words fit the exact layout block, and the visuals reinforce the psychological punch of the headline.

The goal is to remove all excuses a targeted audience of ~900 registered Harvestline + ~1800 Unaffiliated voters in our precinct - have for not voting.

I need to be able to work by phone / online chat to iterate designs
I need to own the design in the top couple of software outputs that any printer service will require.

I want to experiment with very subtle background images as follows:
- Front of postcard that conveys "CHANGE" of not just seasons - but of encouraging change of precinct voter representation - so anything about fall foliage / conveyance of change tie-in is worthy of considering
- Back of postcard - any Appalachian long rage mountain view that includes 5-7 layers of hills in the distance.
Some photos as samples to consider.

Target Market(s)

~2,700 registered Harvestliners and Unaffiliated voters

Requirements
Must have
• We require BOTH persuasive copy and high-impact layout for an oversized 6x11 political mailer. This might be one person, but it likely requires a specialized "creative team." of an experienced political strategist copywriter PLUS a graphic designer - so the words fit the exact layout block, and the visuals reinforce the psychological punch of the headline
Nice to have
• subtle background photos

```html
<!DOCTYPE html>
<html lang="en">
<head>
<meta charset="utf-8">
<title>Vote for Change – Postcard Front</title>
<link rel="stylesheet" href="https://fonts.googleapis.com/css2?family=Anton&family=Oswald:wght@500;600;700&family=Montserrat:wght@800&display=swap">
<style>
  :root{
    --page:#ffffff;
    --ink:#111111;
    --gold:#f8b81a;
    --white:#ffffff;
    --bark:#3a2118;
    --rust:#7a3f22;
    --amber:#d98a1c;
    --slate:#2e3a3c;
    --navy:#2c2f6e;
    --lavender:#7377c4;
  }
  *{box-sizing:border-box;margin:0;padding:0}
  html,body{width:1200px;height:743px;overflow:hidden;background:var(--page)}
  .canvas{position:relative;width:1200px;height:743px}
  .side-label{
    position:absolute;top:52px;left:0;width:1200px;text-align:center;
    font:800 34px/1 "Montserrat",sans-serif;letter-spacing:22px;color:var(--ink);
    padding-left:22px;
  }
  .postcard{position:absolute;left:92px;top:103px;width:1008px;height:556px;overflow:hidden}
  .backdrop{
    position:absolute;inset:0;
    background:
      radial-gradient(ellipse 260px 230px at 760px 390px, var(--amber) 0%, rgba(217,138,28,.55) 45%, rgba(217,138,28,0) 75%),
      radial-gradient(ellipse 300px 260px at 950px 120px, var(--slate) 0%, rgba(46,58,60,0) 80%),
      linear-gradient(100deg, var(--bark) 0%, #4a2a1c 45%, var(--rust) 70%, #3c3533 100%);
  }
  .issue{position:absolute;display:flex;align-items:center;gap:7px;white-space:nowrap;
    font:600 21px/1 "Oswald",sans-serif;color:var(--white);letter-spacing:.2px}
  .issue svg{width:38px;height:38px;flex:none}
  .headline{position:absolute;left:55px;font-family:"Anton",sans-serif;line-height:1;white-space:nowrap;font-weight:400}
  .headline-top{top:152px;font-size:96px;color:var(--white);letter-spacing:6px}
  .headline-main{top:238px;font-size:134px;color:var(--gold);letter-spacing:8px}
  .subhead{position:absolute;left:61px;top:368px;display:flex;align-items:flex-end;gap:9px;color:var(--white);font-family:"Oswald",sans-serif;white-space:nowrap}
  .subhead-lead{font-weight:500;font-size:23px;line-height:1;border-bottom:4px double var(--amber);padding-bottom:3px;margin-bottom:4px}
  .subhead-main{font-weight:600;font-size:42px;line-height:1;letter-spacing:0}
  .band{position:absolute;left:0;bottom:0;width:1008px;height:68px;background:var(--navy);
    display:flex;align-items:center;padding-left:163px;white-space:nowrap}
  .band-badge{width:36px;height:36px;margin-right:9px;flex:none}
  .band-call{font:700 38px/1 "Oswald",sans-serif;color:var(--white);letter-spacing:1px}
  .band-tagline{font:700 28px/1 "Oswald",sans-serif;color:var(--lavender);margin-left:22px;letter-spacing:.5px}
  .sign{position:absolute;left:31px;top:428px;width:110px;height:128px;
    background:linear-gradient(180deg,var(--gold) 0%,var(--gold) 62%,#f2a57c 62%,#e98b62 100%);
    border-radius:4px}
</style>
</head>
<body>
<div class="canvas">
  <div class="side-label">FRONT</div>

  <section class="postcard">
    <div class="backdrop" role="img" aria-label="Photo of dark fallen autumn leaves on wet stone with one bright golden maple leaf on the right"></div>

    <div class="issue" style="left:54px;top:43px"><svg viewBox="0 0 38 38"><circle cx="19" cy="19" r="17.5" fill="none" stroke="var(--gold)" stroke-width="1.6"/><path d="M11 26h16M13 26v-6M18 26v-9M23 26v-12" stroke="var(--white)" stroke-width="1.6" fill="none"/></svg>FAMILY BUGET</div>
    <div class="issue" style="left:241px;top:43px"><svg viewBox="0 0 38 38"><circle cx="19" cy="19" r="17.5" fill="none" stroke="var(--gold)" stroke-width="1.6"/><path d="M19 13v12M13 19h12" stroke="var(--white)" stroke-width="2.2"/></svg>HEALTH</div>
    <div class="issue" style="left:364px;top:43px"><svg viewBox="0 0 38 38"><circle cx="19" cy="19" r="17.5" fill="none" stroke="var(--gold)" stroke-width="1.6"/><path d="M19 11v16M12 14h14M12 14l-3 7h6zM26 14l-3 7h6zM15 27h8" stroke="var(--white)" stroke-width="1.5" fill="none"/></svg>REPRODUCTIVE RIGHTS</div>
    <div class="issue" style="left:620px;top:43px"><svg viewBox="0 0 38 38"><circle cx="19" cy="19" r="17.5" fill="none" stroke="var(--gold)" stroke-width="1.6"/><path d="M19 9l8 3v7c0 5-4 8-8 10-4-2-8-5-8-10v-7z" stroke="var(--white)" stroke-width="1.5" fill="none"/><path d="M16 14v10M22 14v10" stroke="var(--white)" stroke-width="1.5"/></svg>FOOD SECURITY</div>

    <div class="issue" style="left:54px;top:89px"><svg viewBox="0 0 38 38"><circle cx="19" cy="19" r="17.5" fill="none" stroke="var(--gold)" stroke-width="1.6"/><path d="M9 14c4-2 7-2 10 1 3-3 6-3 10-1v12c-4-2-7-2-10 1-3-3-6-3-10-1zM19 15v12" stroke="var(--white)" stroke-width="1.5" fill="none"/></svg>EDUCATION</div>
    <div class="issue" style="left:212px;top:89px"><svg viewBox="0 0 38 38"><circle cx="19" cy="19" r="17.5" fill="none" stroke="var(--gold)" stroke-width="1.6"/><path d="M10 19l9-8 9 8M13 17v10h12V17M17 27v-5h4v5" stroke="var(--white)" stroke-width="1.5" fill="none"/></svg>HOUSING</div>
    <div class="issue" style="left:348px;top:89px"><svg viewBox="0 0 38 38"><circle cx="19" cy="19" r="17.5" fill="none" stroke="var(--gold)" stroke-width="1.6"/><path d="M21 9l-7 11h6l-2 9 7-11h-6z" stroke="var(--white)" stroke-width="1.5" fill="none"/></svg>ENERGY</div>
    <div class="issue" style="left:474px;top:89px"><svg viewBox="0 0 38 38"><circle cx="19" cy="19" r="17.5" fill="none" stroke="var(--gold)" stroke-width="1.6"/><circle cx="19" cy="19" r="9" stroke="var(--white)" stroke-width="1.5" fill="none"/><path d="M10 19h18M19 10c-4 5-4 13 0 18M19 10c4 5 4 13 0 18" stroke="var(--white)" stroke-width="1.2" fill="none"/></svg>ENVIRONMENT</div>

    <h1 class="headline headline-top">VOTE FOR</h1>
    <div class="headline headline-main">CHANGE</div>

    <p class="subhead"><span class="subhead-lead">FOR A</span><span class="subhead-main">NEW REPRESENTATION</span></p>

    <div class="band">
      <svg class="band-badge" viewBox="0 0 36 36"><circle cx="18" cy="18" r="15" fill="none" stroke="var(--gold)" stroke-width="4" stroke-dasharray="4 2"/><path d="M11 18l5 5 9-10" stroke="var(--gold)" stroke-width="3.2" fill="none" stroke-linecap="round" stroke-linejoin="round"/></svg>
      <span class="band-call">VOTE HARVESTLINER</span>
      <span class="band-tagline">FOR PEOPLE. FOR YOUR FUTURE</span>
    </div>

    <div class="sign" role="img" aria-label="Illustration of a hand raising a yellow VOTE placard"></div>
  </section>
</div>
</body>
</html>
```